Layout und Text für Mailing
Zielgruppe
Wir kaufen und verkaufen gebrauchte Werkzeugmaschinen. Hier geht es um die Anfrage nach gebrauchten Werkzeugmaschinen, die evtl. zum Verkauf stehen. Zielgruppe hier sind Firmen aber auch berufliche Schulen, Behindertenwerkstätten, JVAs die mit Werkzeugmaschinen arbeiten.
Aufgabenstellung
Anschreiben als Serienbrief bestehend aus einem DINA4 Blatt, Faxformular für Antwort auf dem Blatt, Hinweis auf Antwortmöglichkeit per Mail. Wichtig ist Hinweis, dass wir Abbau, Verladung und Transport komplett abwickeln. Verwendung des Firmenbriefpapiers nicht zwingend erforderlich. Die im Fußteil genannten Bedingungen müssen nicht hervorgehoben werden bzw. es genügt ein Hinweis auf unsere AGBs.

```html
<!DOCTYPE html>
<html lang="de">
<head>
<meta charset="utf-8">
<title>Mailing – Wir kaufen Ihre Gebrauchtmaschinen</title>
<link rel="stylesheet" href="https://fonts.googleapis.com/css2?family=Roboto+Condensed:wght@700&family=Arimo:wght@400;700&display=swap">
<style>
  :root {
    --red: #e1251b;
    --peach: #fadfd3;
    --white: #ffffff;
    --ink: #3a3a3a;
    --slate: #48494b;
    --rule: #b9b9b9;
    --stage: #efefef;
    --sign: #dfe3ef;
  }
  * { margin: 0; padding: 0; box-sizing: border-box; }
  html, body { width: 716px; height: 1200px; overflow: hidden; }
  body { background: var(--stage); font-family: "Arimo", Arial, sans-serif; color: var(--ink); position: relative; }
  .sheet { position: absolute; left: 0; top: 251px; width: 716px; height: 698px; }
  .abs { position: absolute; }
  .cond { font-family: "Roboto Condensed", "Arial Narrow", sans-serif; font-weight: 700; }

  /* brand card and colour strips */
  .brand-card { left: 0; top: 0; width: 222px; height: 278px; background: var(--white); }
  .strip { left: 0; width: 222px; }
  .strip--peach { top: 279px; height: 139px; background: var(--peach); }
  .strip--red { top: 418px; height: 139px; background: var(--red); }
  .strip--slate { top: 557px; height: 138px; background: var(--slate); }
  .divider { left: 222px; top: 0; width: 5px; height: 696px; background: var(--rule); }
  .baseline { left: 0; top: 695px; width: 716px; height: 3px; background: var(--rule); }

  /* company name block: plain square + name in text font */
  .brand-square { background: var(--red); }
  .brand-name { font-family: "Arimo", Arial, sans-serif; font-weight: 700; color: var(--ink); line-height: 1.15; }

  .card-square { left: 40px; top: 59px; width: 144px; height: 139px; }
  .card-name { left: 40px; top: 204px; font-size: 15px; }

  /* letter */
  .letter { left: 227px; top: 0; width: 489px; height: 695px; background: var(--white); }
  .letter-column { left: 258px; top: 0; width: 155px; height: 695px; background: var(--peach); }
  .band { background: var(--red); }
  .band--head-left { left: 227px; top: 59px; width: 31px; height: 103px; }
  .band--head-right { left: 413px; top: 59px; width: 303px; height: 103px; }
  .band--foot-left { left: 227px; top: 625px; width: 31px; height: 70px; }
  .band--foot-right { left: 413px; top: 625px; width: 303px; height: 70px; }

  .letter-square { left: 282px; top: 59px; width: 108px; height: 103px; }
  .letter-name { left: 283px; top: 166px; font-size: 9.5px; }

  .headline { left: 436px; top: 101px; color: var(--white); font-size: 17px; line-height: 1.12; }
  .date { right: 20px; top: 166px; font-size: 10px; }

  .sender { left: 283px; top: 199px; width: 125px; font-size: 7.4px; line-height: 1.2; font-style: normal; }
  .sender p { margin-bottom: 5.6px; }
  .sender p.gap { margin-bottom: 9px; }

  .body-copy { left: 436px; top: 199px; width: 260px; font-size: 9.6px; line-height: 1.25; }
  .body-copy p { margin-bottom: 11.5px; }
  .signature { left: 445px; top: 386px; width: 198px; height: 30px; background: var(--sign); }
  .signer { left: 436px; top: 414px; font-size: 9.6px; }

  .tag { color: var(--white); background: var(--red); font-size: 16px; line-height: 23px; padding-left: 10px; }
  .tag--answer { left: 283px; top: 457px; width: 107px; height: 23px; }
  .tag--fax { left: 436px; top: 457px; width: 260px; height: 23px; }
  .tag--terms { left: 282px; top: 625px; width: 106px; height: 24px; border: 1px solid var(--white); border-top: 0; }

  .reply { left: 436px; top: 500px; width: 262px; font-size: 9.6px; line-height: 1.25; }
  .reply p { margin-bottom: 12.5px; }
  .reply p.space { margin-bottom: 24px; }
  .online { left: 436px; top: 597px; font-size: 10px; }

  .terms { left: 436px; top: 641px; width: 260px; font-size: 6.5px; line-height: 1.22; color: var(--white); text-align: justify; }
</style>
</head>
<body>
<main class="sheet">
  <div class="abs brand-card"></div>
  <div class="abs brand-square card-square"></div>
  <div class="abs brand-name card-name">Konrad Hellmann<br>Werkzeugmaschinen</div>
  <div class="abs strip strip--peach"></div>
  <div class="abs strip strip--red"></div>
  <div class="abs strip strip--slate"></div>
  <div class="abs divider"></div>

  <div class="abs letter"></div>
  <div class="abs letter-column"></div>
  <div class="abs band band--head-left"></div>
  <div class="abs band band--head-right"></div>
  <div class="abs band band--foot-left"></div>
  <div class="abs band band--foot-right"></div>

  <div class="abs brand-square letter-square"></div>
  <div class="abs brand-name letter-name">Konrad Hellmann<br>Werkzeugmaschinen</div>

  <h1 class="abs headline cond">Wir kaufen<br>Ihre Gebrauchtmaschinen</h1>
  <div class="abs date cond">Datum</div>

  <address class="abs sender">
    <p class="gap">Konrad Hellmann<br>Werkzeugmaschinen</p>
    <p class="gap">Lindenweg 12<br>D-64711 Auenstadt</p>
    <p>Telefon: 06071 -5520</p>
    <p>Telefax: 06071 -5231</p>
    <p>E-Mail: info@hk-wm.de</p>
    <p>Homepage: www.hk-wm.de</p>
    <p>Ust-Id Nr.: DE 274019388</p>
    <p>Kreisbank Talgrund</p>
    <p>Konto-Nr.: 310 284 500</p>
    <p>Bankleitzahl: 507 422 19</p>
    <p>IBAN:<br>DE 4450 7422 1903 1028 4500</p>
    <p>BIC: KRTB DE 51 AUE</p>
    <p>SWFT: KRTB DE FF</p>
  </address>

  <div class="abs body-copy">
    <p>Sehr geehrte Damen und Herren,</p>
    <p>wir kaufen Gebrauchtmaschinen an und sorgen für eine reibungslose Abwicklung bezüglich Abbau, Verladung und Transport.</p>
    <p>Unser Spezialgebiet sind Gebrauchtmaschinen der Metall-<br>bearbeitung. Gerne können Sie uns auch Maschinen aus anderen Bereichen wie Holzbearbeitung, Kunststoffbear-<br>beitung, etc. anbieten.</p>
    <p>Für weitere Informationen stehen wir Ihnen gern persön-<br>lich zur Verfügung.</p>
    <p>Mit freundlichen Grüßen</p>
  </div>
  <div class="abs signature" role="img" aria-label="Handschriftliche Unterschrift"></div>
  <div class="abs signer">Konrad Hellmann</div>

  <div class="abs tag tag--answer cond">Antwort</div>
  <div class="abs tag tag--fax cond">Fax 06071-5231</div>

  <div class="abs reply">
    <p>Ja, wir haben Gebrauchtmaschinen zu verkaufen.</p>
    <p class="space">Bitte rufen Sie uns zurück unter:</p>
    <p>Ansprechparter:</p>
  </div>
  <div class="abs online cond">Besuchen Sie uns online unter: www.hk-wm.de</div>

  <div class="abs tag tag--terms cond">Bedingungen</div>
  <p class="abs terms">Zahlungs- und Lieferbedingungen: Zahlung bei Übernahme in Bar oder mit bankbe-<br>stätigtem Scheck. Preis gilt ab Standort, zzgl. MwSt. Zwischenverkauf und Irrtum der technischen Daten vorbehalten. Verkauf von Gebrauchtmaschinen ohne jegliche Gewährleistung. Es gelten unsere Allgemeinen Geschäftsbedingungen. www.agb.maschinenhandel-muster.de</p>

  <div class="abs baseline"></div>
</main>
</body>
</html>
```